Lumo4Kart - a fintech company - business card

We need a business card design for our Payments Technology company in Sydney, Australia. We provide business with payment solutions expanding across EFTPOS machines, online payment gateways and mobile payment solutions. We would like to see designs that are clean, classy and professional.
Target Market(s)
Business professionals, executives, c-suite
Industry/Entity Type
Fintech
Contact Information for Business Card
Will be on 400gsm. Logo will most likely be spot gloss unless designer recommends otherwise.
Font styles to use
Sans Serif
Requirements
Must have
- We need our website (lumo4kart.com.au), email (contact@lumo4kart.com.au), mobile (0432 587 904) and direct phone number (02 6815 3927) to feature on the card along with our logo (attached) and the words "EFTPOS | ONLINE | MOBILE"
- Font = Roboto

```html
<!DOCTYPE html>
<html lang="en">
<head>
<meta charset="utf-8">
<title>Lumo4Kart – Business Card</title>
<link rel="stylesheet" href="https://fonts.googleapis.com/css2?family=Roboto:wght@300;700&display=swap">
<style>
  :root {
    --backdrop: #e4e4e4;
    --card-blue: #2a97c6;
    --card-blue-deep: #2389b8;
    --ink-white: #ffffff;
  }
  * { margin: 0; padding: 0; box-sizing: border-box; }
  html, body {
    width: 1200px;
    height: 900px;
    overflow: hidden;
    background: var(--backdrop);
    font-family: "Roboto", sans-serif;
  }
  .canvas {
    position: relative;
    width: 1200px;
    height: 900px;
  }
  .business-card {
    position: absolute;
    left: 150px;
    top: 175px;
    width: 900px;
    height: 550px;
    background: linear-gradient(160deg, var(--card-blue) 0%, var(--card-blue-deep) 100%);
    overflow: hidden;
    color: var(--ink-white);
  }
  .brand {
    position: absolute;
    left: 36px;
    top: 236px;
    display: flex;
    align-items: center;
    gap: 12px;
    white-space: nowrap;
  }
  .brand-dot {
    width: 26px;
    height: 26px;
    border-radius: 50%;
    background: var(--ink-white);
  }
  .brand-name {
    font-weight: 700;
    font-size: 30px;
    color: var(--ink-white);
  }
  .service-line {
    position: absolute;
    left: 270px;
    top: 296px;
    font-weight: 700;
    font-size: 30px;
    letter-spacing: 0.26em;
    white-space: nowrap;
  }
  .service-line .divider {
    font-weight: 300;
    margin: 0 0.3em;
  }
  .contact-block {
    position: absolute;
    left: 270px;
    top: 360px;
    display: flex;
    align-items: flex-start;
    gap: 22px;
    font-weight: 300;
    font-size: 24px;
    line-height: 1.35;
    white-space: nowrap;
  }
  .contact-column { display: flex; flex-direction: column; }
  .contact-bullets {
    display: flex;
    flex-direction: column;
    font-weight: 700;
    font-size: 18px;
    line-height: 32.4px;
  }
</style>
</head>
<body>
  <main class="canvas">
    <section class="business-card" aria-label="Lumo4Kart business card">
      <div class="brand">
        <span class="brand-dot" aria-hidden="true"></span>
        <span class="brand-name">Lumo4Kart</span>
      </div>
      <p class="service-line">EFTPOS<span class="divider">|</span>ONLINE<span class="divider">|</span>MOBILE</p>
      <div class="contact-block">
        <div class="contact-column">
          <span class="contact-web">lumo4kart.com.au</span>
          <span class="contact-mobile">0432 587 904 (Mob)</span>
        </div>
        <div class="contact-bullets" aria-hidden="true">
          <span>•</span>
          <span>•</span>
        </div>
        <div class="contact-column">
          <span class="contact-email">contact@lumo4kart.com.au</span>
          <span class="contact-phone">02 6815 3927 (Ph)</span>
        </div>
      </div>
    </section>
  </main>
</body>
</html>
```